Business cards for property management company

Need new business cards designed for our property management company and rental community, Blue Fern Commons. These cards will be primarily picked up by rental applicants.

May be single or double sided design.

I need cards for two different people, listed below. The design can be the same for both, and the only information that will be different is name and email address.

Industry/Entity Type

Property Management

Requirements
Must have
• US standard business card - 2''x3.5'' horizontal design.

1. Logo (attached). The text does not have to stay below the logo, but the card does need to say "Blue Fern Commons" somewhere on it (does not have to be same font as logo, but those fonts are Americana Extra Bold and BlackJack if needed).
2. Name: one with "Paula Whitcombe" and one with "Darrell Whitcombe"
3. Email address: one with "paula@bluefernhome.com" and one with "darrell@bluefernhome.com"
4. Web address: bluefernhome.com
5. Phone: 281.604.2218
6. Address: 1783 Wexford Lane, Porterfield, Texas 77812 (zip code may me omitted, at your discretion)
Should not have
• No rounded corners or special cuts.

No bevel, emboss or shadow effects.

As a note, please do not use our website as a basis for color or design schemes. We are working on a redesign, based around the new logo (attached to brief).

```html
<!DOCTYPE html>
<html lang="en">
<head>
<meta charset="utf-8">
<title>Blue Fern Commons – Business Cards</title>
<link rel="stylesheet" href="https://fonts.googleapis.com/css2?family=Open+Sans:wght@400;600;700&display=swap">
<style>
  :root {
    --backdrop: #4d4d4d;
    --card-paper: #ececec;
    --brand-blue: #0fa3c9;
    --brand-green: #3f9a3c;
    --ink-dark: #4a4a4a;
    --ink-mid: #5a5a5a;
    --white: #ffffff;
  }
  * { box-sizing: border-box; margin: 0; padding: 0; }
  html, body {
    width: 1200px;
    height: 987px;
    overflow: hidden;
  }
  body {
    background: var(--backdrop);
    font-family: "Open Sans", Arial, sans-serif;
    position: relative;
  }
  .card {
    position: absolute;
    width: 480px;
    height: 274px;
    overflow: hidden;
    background: var(--card-paper);
  }
  .card--darrell { left: 390px; top: 80px; }
  .card--paula   { left: 130px; top: 440px; }
  .card--back    { left: 650px; top: 600px; background: var(--brand-blue); }

  .card__waves {
    position: absolute;
    inset: 0;
    width: 100%;
    height: 100%;
  }
  .wave--blue  { fill: var(--brand-blue); }
  .wave--green { fill: var(--brand-green); }

  .brand-name {
    position: absolute;
    left: 28px;
    top: 100px;
    display: flex;
    align-items: center;
    gap: 8px;
    font-size: 19px;
    font-weight: 700;
    color: var(--brand-green);
    white-space: nowrap;
  }
  .brand-name__dot {
    width: 12px;
    height: 12px;
    border-radius: 50%;
    background: var(--brand-blue);
  }

  .contact {
    position: absolute;
    left: 262px;
    top: 38px;
    color: var(--ink-mid);
    font-size: 13px;
    line-height: 19px;
  }
  .contact__name {
    font-size: 16px;
    font-weight: 700;
    color: var(--ink-dark);
    text-transform: uppercase;
    letter-spacing: 0.3px;
    margin-bottom: 4px;
  }

  .card__address {
    position: absolute;
    left: 0;
    right: 0;
    bottom: 22px;
    text-align: center;
    color: var(--white);
    font-size: 11.5px;
    font-weight: 600;
    text-transform: uppercase;
    letter-spacing: 0.2px;
  }

  .back__brand {
    position: absolute;
    right: 44px;
    top: 118px;
    display: flex;
    align-items: center;
    gap: 8px;
    color: var(--white);
    font-size: 22px;
    font-weight: 700;
    white-space: nowrap;
  }
  .back__brand-square {
    width: 12px;
    height: 12px;
    background: var(--white);
  }
  .back__details {
    position: absolute;
    right: 44px;
    top: 186px;
    text-align: right;
    color: var(--white);
    font-size: 12.5px;
    line-height: 22px;
    font-weight: 600;
    text-transform: uppercase;
  }
  .back__web { text-transform: none; }
</style>
</head>
<body>

  <article class="card card--darrell">
    <svg class="card__waves" viewBox="0 0 480 274" preserveAspectRatio="none" aria-hidden="true">
      <path class="wave--green" d="M0,182 C140,146 300,136 410,144 L410,156 C300,152 140,162 0,198 Z"/>
      <path class="wave--blue" d="M0,198 C150,164 280,156 380,158 C440,158 470,112 480,82 L480,274 L0,274 Z"/>
    </svg>
    <div class="brand-name"><span class="brand-name__dot"></span>Blue Fern Commons</div>
    <div class="contact">
      <p class="contact__name">Darrell Whitcombe</p>
      <p>Phone: 281.604.2218</p>
      <p>darrell@bluefernhome.com</p>
      <p>www.bluefernhome.com</p>
    </div>
    <p class="card__address">1783 Wexford Lane - Porterfield, Texas 77812</p>
  </article>

  <article class="card card--paula">
    <svg class="card__waves" viewBox="0 0 480 274" preserveAspectRatio="none" aria-hidden="true">
      <path class="wave--green" d="M0,182 C140,146 300,136 410,144 L410,156 C300,152 140,162 0,198 Z"/>
      <path class="wave--blue" d="M0,198 C150,164 280,156 380,158 C440,158 470,112 480,82 L480,274 L0,274 Z"/>
    </svg>
    <div class="brand-name"><span class="brand-name__dot"></span>Blue Fern Commons</div>
    <div class="contact">
      <p class="contact__name">Paula Whitcombe</p>
      <p>Phone: 281.604.2218</p>
      <p>paula@bluefernhome.com</p>
      <p>www.bluefernhome.com</p>
    </div>
    <p class="card__address">1783 Wexford Lane - Porterfield, Texas 77812</p>
  </article>

  <article class="card card--back">
    <div class="back__brand"><span class="back__brand-square"></span>Blue Fern Commons</div>
    <div class="back__details">
      <p>1783 Wexford Ln. Porterfield, TX 77812</p>
      <p class="back__web">www.bluefernhome.com</p>
    </div>
  </article>

</body>
</html>
```